International Trading Company, 'KIRO' needs a Business Card

The company name is "KIRO" and it has own logo design.
I'd like to use its logo on this business card.
I need two side Business Card.
I'll look forward to your great design.
Thank you very much in advance.

Contact Information for Business Card

Company Name : Kiro Harbour Limited
Information Example
Dorian Pallister
Mobile(use icon please) : 1 (212) 555-0143
Tel(use icon please) : 1 (212) 555-0178
Email(use icon please) : dorian27@kiroharbour-mail.com
Address(use icon please) : 482 Halden Ave, New York, NY 10160, USA

```html
<!DOCTYPE html>
<html lang="en">
<head>
<meta charset="utf-8">
<title>Kiro Harbour Limited — Business Card</title>
<link rel="stylesheet" href="https://fonts.googleapis.com/css2?family=Lato:wght@400;700;900&display=swap">
<style>
  :root {
    --canvas-bg: #e6e5e3;
    --card-dark: #3b3b3d;
    --card-light: #ffffff;
    --logo-white: #ffffff;
    --ink-strong: #555555;
    --ink-body: #5a5a5a;
    --ink-faint: #efefef;
    --card-shadow: rgba(0, 0, 0, 0.18);
  }
  * { box-sizing: border-box; margin: 0; padding: 0; }
  html, body {
    width: 1200px;
    height: 780px;
    overflow: hidden;
    background: var(--canvas-bg);
    font-family: "Lato", Arial, sans-serif;
  }
  .canvas {
    position: relative;
    width: 1200px;
    height: 780px;
    display: flex;
    align-items: center;
    justify-content: center;
    gap: 48px;
  }
  .card {
    position: relative;
    width: 520px;
    height: 297px;
    border-radius: 3px;
    overflow: hidden;
    box-shadow: 0 10px 28px var(--card-shadow);
  }
  /* Front side */
  .card--front {
    background: var(--card-dark);
    display: flex;
    align-items: center;
    justify-content: center;
  }
  .front-logo {
    color: var(--logo-white);
    font-weight: 900;
    font-size: 88px;
    letter-spacing: 3px;
    line-height: 1;
  }
  /* Back side */
  .card--back {
    background: var(--card-light);
    padding: 38px 0 0 40px;
  }
  .company-name {
    position: relative;
    z-index: 1;
    color: var(--ink-strong);
    font-weight: 700;
    font-size: 24px;
    letter-spacing: 0.2px;
  }
  .contact {
    position: relative;
    z-index: 1;
    margin-top: 34px;
    color: var(--ink-body);
    font-size: 13px;
    line-height: 1.45;
  }
  .contact-name {
    font-weight: 700;
    font-size: 15px;
    color: var(--ink-strong);
    margin-bottom: 4px;
  }
  .contact-address { margin-bottom: 2px; }
  .contact-line {
    display: flex;
    align-items: center;
    gap: 7px;
  }
  .contact-icon {
    width: 12px;
    height: 12px;
    flex: none;
    fill: var(--ink-body);
  }
  .back-watermark {
    position: absolute;
    right: 16px;
    bottom: 18px;
    writing-mode: vertical-rl;
    transform: rotate(180deg);
    color: var(--ink-faint);
    font-weight: 900;
    font-size: 72px;
    letter-spacing: 2px;
    line-height: 1;
    pointer-events: none;
  }
</style>
</head>
<body>
<main class="canvas">
  <section class="card card--front" aria-label="Business card front">
    <div class="front-logo">ZUVRO</div>
  </section>

  <section class="card card--back" aria-label="Business card back">
    <div class="back-watermark" aria-hidden="true">ZUVRO</div>
    <h1 class="company-name">Kiro Harbour Limited</h1>
    <div class="contact">
      <p class="contact-name">Dorian Pallister</p>
      <p class="contact-address">482 Halden Ave, New York,<br>NY 10160, USA</p>
      <p class="contact-line">
        <svg class="contact-icon" viewBox="0 0 12 12" aria-hidden="true"><path d="M3 0h6a1 1 0 0 1 1 1v10a1 1 0 0 1-1 1H3a1 1 0 0 1-1-1V1a1 1 0 0 1 1-1zm0 1.5v7.5h6V1.5zm3 8.3a.7.7 0 1 0 0 1.4.7.7 0 0 0 0-1.4z"/></svg>
        1 (212) 555-0143
      </p>
      <p class="contact-line">
        <svg class="contact-icon" viewBox="0 0 12 12" aria-hidden="true"><path d="M1 3.2C1 2 2.5 1 6 1s5 1 5 2.2V4H8.5V3H3.5v1H1zM3 5h6l2 3v3H1V8zm3 1.2a1.6 1.6 0 1 0 0 3.2 1.6 1.6 0 0 0 0-3.2z"/></svg>
        1 (212) 555-0178
      </p>
      <p class="contact-line">
        <svg class="contact-icon" viewBox="0 0 12 12" aria-hidden="true"><path d="M0 2h12v8H0zm1 1v.3l5 3.4 5-3.4V3zm0 1.5V9h10V4.5L6 7.9z"/></svg>
        dorian27@kiroharbour-mail.com
      </p>
    </div>
  </section>
</main>
</body>
</html>
```